Flyer-Design für Vermietung und Verkauf von Palettenmöbeln
Zielgruppe
Ich vermiete und verkaufe in Tischler-Handarbeit hergestellte Palettenmöbel aus recycelten Paletten, wobei mein Schwerpunkt bei der Vermietung liegt. Meine Zielgruppe sind alle, die Veranstaltungen, Events , Messen, Präsentationen, private Feiern und Ähnliches planen und organisieren. Große und kleine Firmen, senatseigene Stellen, Privatpersonen, aber der Schwerpunkt liegt bei den Eventagenturen, welche mit der Organisation verschiedenster Veranstaltungen beauftragt werden.
Aufgabenstellung
Ich hätte ein klares und modernes Design mit BÄHM-Charakter. Der Flyer soll ein Hingucker sein, aber den Betrachter nicht erschlagen. Das Thema Nachhaltigkeit (die Möbel sind aus recylten Paletten) sollte bedacht werden. Ich hätte gern einen Faltflyer in DIN lang Größe. Dies ist für einen Mailing-Versand besser geeignet. Ich liefere eigene Bilder, aber sollten ein Stock-Bilder hilfreich sein, können dies gern verwendet werden. Ich habe natürlich noch mehr Bilder und kann diese gern zur Verfügung stellen, wenn ich weiß was benötigt wird. Es soll nicht viel Text in den Flyer. Ich bin hier sehr dankbar für Vorschläge, da ich mich mit dem Text sehr schwer tue. Ich hoffe, die Profis können mir auch beim Text helfen. Ich stelle auch Fotos meines alten Flyer zur Verfügung. Dieser ist definitv zu konservativ, langweilig und veraltet. Ich brauche ein modernes, hippes Design mit überzeugendem Text.

```html
<!DOCTYPE html>
<html lang="de">
<head>
<meta charset="utf-8">
<title>Palettenmöbel Faltflyer – Innenseite</title>
<link href="https://fonts.googleapis.com/css2?family=Montserrat:wght@400;500;700&display=swap" rel="stylesheet">
<style>
  :root{
    --green:#7ab648;
    --grey-box:#ececec;
    --paper:#ffffff;
    --bg:#e4e4e4;
    --text:#4a4a4a;
    --heading:#555555;
    --fold:#dedede;
  }
  *{margin:0;padding:0;box-sizing:border-box}
  html,body{width:1200px;height:764px;overflow:hidden;background:var(--bg)}
  body{font-family:"Montserrat",sans-serif;color:var(--text)}
  .spread{position:absolute;left:105px;top:32px;width:990px;height:700px;background:var(--paper);box-shadow:0 6px 24px rgba(0,0,0,.12)}
  .fold{position:absolute;top:0;bottom:0;width:1px;background:var(--fold);z-index:5}
  .fold--1{left:330px}.fold--2{left:660px}

  .photo{position:absolute}
  .photo--terrace{left:40px;top:40px;width:320px;height:260px;background:linear-gradient(160deg,#e7e9ec 0%,#cfc7bb 45%,#a98a63 100%)}
  .photo--bench{left:105px;top:230px;width:225px;height:180px;background:linear-gradient(180deg,#f2f0ec 0%,#d6b994 60%,#b08457 100%)}
  .photo--event{left:590px;top:270px;width:400px;height:200px;background:linear-gradient(135deg,#c24a9a 0%,#a4553a 40%,#8a4a2a 70%,#d58a4a 100%)}

  .product{position:absolute;background:linear-gradient(180deg,#e2c39a,#b98a57);border-radius:2px}
  .product--stools{left:440px;top:600px;width:110px;height:70px}
  .product--bar{left:580px;top:590px;width:140px;height:70px}
  .product--cart{left:760px;top:585px;width:110px;height:75px}

  .tag{position:absolute;left:20px;top:80px;width:110px;height:28px;background:var(--green);color:#fff;font-size:11px;font-weight:500;letter-spacing:1px;line-height:28px;padding-left:16px}
  .tick{position:absolute;background:var(--green);z-index:6}

  .grey-box{position:absolute;left:360px;top:40px;width:590px;height:230px;background:var(--grey-box)}
  .wishes{position:absolute;left:28px;top:48px;width:240px;height:170px}
  .wishes .note{position:absolute;left:0;bottom:0}
  .service{position:absolute;left:330px;top:24px;width:245px}

  .title{font-weight:400;color:var(--heading);line-height:1.15}
  .title--xl{font-size:26px}
  .title--m{font-size:16px;margin-bottom:6px}
  .title--s{font-size:15px;margin:10px 0 4px}
  .amp{color:var(--green)}
  .note{color:var(--green);font-weight:700;font-size:11px;line-height:1.5}
  .copy{font-size:10.5px;line-height:1.55}
  .copy strong{font-weight:700}

  .rustic{position:absolute;left:350px;top:270px;width:240px;height:290px;background:var(--green);color:#fff;padding:22px 20px}
  .rustic h2{font-size:15px;font-weight:500;letter-spacing:.5px;margin-bottom:10px}
  .rustic p{font-size:10px;line-height:1.6;margin-bottom:12px}

  .event-label{position:absolute;left:830px;top:284px;width:145px;background:rgba(255,255,255,.78);padding:7px 12px;text-align:right}
  .event-label .title{font-size:17px}
  .event-label small{display:block;font-size:10px;color:var(--heading)}

  .intro{position:absolute;left:40px;top:440px;width:270px}
  .intro .title{font-size:19px;margin-bottom:12px}
  .intro p{margin-bottom:12px}
  .interest{position:absolute;left:700px;top:488px;width:260px;text-align:right}
  .interest .title{font-size:19px;margin-bottom:10px}
</style>
</head>
<body>
<main class="spread">
  <div class="fold fold--1"></div>
  <div class="fold fold--2"></div>

  <!-- Panel 1 -->
  <div class="photo photo--terrace" role="img" aria-label="Terrasse mit Palettenmöbeln unter weißen Sonnenschirmen"></div>
  <div class="tag">PRODUKTE</div>
  <div class="tick" style="left:60px;top:60px;width:1px;height:20px"></div>
  <div class="tick" style="left:60px;top:120px;width:60px;height:1px"></div>
  <div class="photo photo--bench" role="img" aria-label="Palettenbank mit schwarzem Sitzpolster"></div>
  <section class="intro">
    <h2 class="title">Nicht nur ein Hingucker</h2>
    <p class="copy"><strong>Es ist uns ganz besonders wichtig, dass unsere Möbel nicht nur gut aussehen, sondern man auch bequem und relaxed darauf sitzen kann.</strong></p>
    <p class="copy">Daher vermieten wir unsere Palettenmöbel inklusive Sitzpolster, bestehend aus Schaumstoff, mit hochwertigem flammhemmendem Kunstleder bezogen, verfügbar in schwarz und in rot.</p>
    <p class="note" style="text-align:right">Sitzpolster in Wunschfarbe sind<br>gegen Aufpreis möglich.</p>
  </section>

  <!-- Panel 2 + 3 grey band -->
  <div class="grey-box">
    <section class="wishes">
      <h2 class="title title--xl">Nach Ihren<br>Wünschen</h2>
      <p class="note">Für individuelle<br>Wünsche sprechen<br>Sie uns einfach an!</p>
    </section>
    <section class="service">
      <h2 class="title title--m">Lieferung, Aufbau <span class="amp">&amp;</span> Abholung</h2>
      <p class="copy">Gern übernehmen wir für Sie die Lieferung, den Aufbau und die Abholung Ihrer Möbelstücke in Berlin und Umgebung.</p>
      <h3 class="title title--s">Gestaltung</h3>
      <p class="copy">Gerne übernehmen wir die farbliche Gestaltung der Sitzkissen nach Ihren Wünschen – z.B. in Ihrer Firmenfarbe.</p>
    </section>
  </div>
  <div class="tick" style="left:660px;top:120px;width:1px;height:20px"></div>
  <div class="tick" style="left:960px;top:40px;width:30px;height:1px"></div>

  <section class="rustic">
    <h2>SCHÖN RUSTIKAL</h2>
    <p>Da unsere Möbel in liebevoller Handarbeit aus recycelten Europaletten erstellt werden, ist jedes Stück einzigartig und weist unterschiedliche Beschaffenheit und Gebrauchsspuren auf.</p>
    <p>Genau dies macht den Charme und den urbanen Charakter unserer Produkte aus. Das Holz bleibt daher größtenteils unbehandelt, wird an relevanten Stellen jedoch geschliffen.</p>
  </section>
  <div class="product product--stools" role="img" aria-label="Stehtisch mit zwei Palettenhockern"></div>
  <div class="product product--bar" role="img" aria-label="Theke aus Paletten"></div>

  <!-- Panel 3 -->
  <div class="photo photo--event" role="img" aria-label="Festsaal mit Palettenmöbeln in pinker Eventbeleuchtung"></div>
  <div class="event-label">
    <div class="title">Ihr Event</div>
    <small>in neuem Licht</small>
  </div>
  <section class="interest">
    <h2 class="title">Interesse bekommen?</h2>
    <p class="note">Werfen Sie einen Blick<br>auf unsere Webseite!<br>Wir freuen uns auf Sie!</p>
  </section>
  <div class="product product--cart" role="img" aria-label="Rollbarer Palettenwagen"></div>
</main>
</body>
</html>
```